Greek Souvlaki Restaurant Menu Design

We would like to redesign our menu (at the moment just a price-list without any graphics) and create something more fun.

You can find all the items we are offering at the following link / our e-shop:
https://olivebranchkitchen.example/orders/en/order/
I have also attached a printout of the above with hand written notes on the sections and items that will be included.

Our menu is divided to a couple of parts:
- Souvlaki Bar and Grill
- Authentic Greek Cuisine
- Wine List
- Desserts
- Bakaliko

This project will take on the first part of our menu, which is the Souvlaki Bar and Grill. If we are happy with your design, we will then develop the rest of our menu.

Souvlaki Bar and Grill
---------------------------

Our souvlaki can be customised to the customer requirements. The following links have similar set ups:

WOW!Patty
https://gr.pinboardly.example/pin/100000000000000001/
I like the way they have set it up, but the graphics and colours used are not my thing. I also like they way they have split up the steps, choose, top it of, etc.

The Krokk
https://gr.pinboardly.example/pin/100000000000000002/
I hate the step 1,2,3 on the left side. It does not make it playful. Like the fact that they have used pictures of the ingredients.

https://gr.pinboardly.example/pin/100000000000000003/
Hate the graphics, like the concept.

-------------

First Sections: Our Souvliaki Pita Wrap

The steps to customise a souvlaki can be found on the following link:
https://olivebranchkitchen.example/orders/en/order/ and choose pita wrap.

Most of the one side of our Souvliaki/Grill menu should be dedicated to our Pita Wraps.

It should have a small description of the Greek Souvlaki Pita Wrap. Something along the lines of "Get a whole meal all wrapped up with our delicious Greek Pita Wraps. Containing protein, sauce and salad". Improvements of this line are welcome.

It should then have the steps to customise it.

Step One.
Choose Base:
1. Chicken Skewer
2. Pork Skewer
3. etc
Price and options can be found on the above link on our website

Step Two.
Add one of our delicious home made sauces.
Options can be found on our website.

Step Three
Finalise it with the ingredients of your choice.
The customer can select multiple incredients

Step Four.
Feeling Hungry? Add extras:
Extras and Prices can be found on the link provided.

Buy two wraps and save. Takeaway only!
You will find this option as "Double Souvlaki Pita Wrap Offer."
Instead of 2x5.5 = £11 pay £10.5. This offer should also be mentioned somewhere on this section.

-----

Second Section - Our Platters

Skewers Platter and Gyros Platter

Options can be found by clicking on the items on the link provided.

Extras and Pita Bread option are common. Meat options are different and skewers have a choice of side. Meat options have 2/3 skewers and 200/300 grams of gyros, so they can probably be combined somehow.

These section can also be called Naked / Open Souvlaki Platters

Third Section
From Our Grill

All options from this section together with modifiers (can be see if you click on each item). I would like pictures from each item.

Forth Section
Meal Deals, starter combo and Set Menu.

Meal Deal for 1/2 and 4 are wraps with extras. The for 4 is not on the pdf and will be up on our website soon, so please check. I think those are easy to e incorporated next to the pita wrap section as upgrades to save.

Set menus are various items.

If they can fit on this page somehow we incorporate them, if not we can make a separate page with the offers / meals deals. If a separate page is created them the meal deal from our kitchen and vegetarean set menu should also be included.

Fifth Section
Salads and Starter

I would like all options from Hot and Cold starter and our salad. I would like pictures next to all options, if possible.

-----

Final notes/ideas.

Wraps, platters and grill could be one page front and back. Salads and starters could be a different page(s) or sections.

The menu should be easily updated and we would like a format where we can update prices and descriptions.

Prices and descriptions can be found on the link provided.

Feel free to improve our descriptions and titles. Please do mention where you made improvements, so we can approve them.

Our kitchen, dessert and wine menu will be given as a separate project and priority will be given to the person that won this competition.

If you need better quality pictures please let us know, most of the pictures we do have them in raw format too.

------

Some designs that I like. To give you an idea of the design I would like to see:

https://www.craftmarketly.example/listing/100000001/american-menu-restaurant-cafe-menus
I would love to see something like that for the grill/salad/starter side of our menu, since it has space for pictures.

https://gr.pinboardly.example/pin/100000000000000004/
I would love to see something like that, where the incredients of a souvlaki come together. This is optional and does not have to be there.

https://gr.pinboardly.example/pin/100000000000000005/

https://gr.pinboardly.example/pin/100000000000000006/

https://gr.pinboardly.example/pin/100000000000000007/

https://gr.pinboardly.example/pin/100000000000000008/

Target Market(s)

London

Font styles to use
Serif
Sans Serif

Colors
abd037
3277b5
33a6d7

Requirements
Must have
• Build your own souvlaki section. See description for examples.

Pictures for starters and salads.

Should be elegant
Nice to have
• Incorporate our relevant meal deals on the souvlaki pita section

```html
<!DOCTYPE html>
<html lang="en">
<head>
<meta charset="utf-8">
<title>Open Souvlaki Platters – Olive Branch Kitchen</title>
<link rel="stylesheet" href="https://fonts.googleapis.com/css2?family=Amatic+SC:wght@400;700&display=swap">
<style>
  :root{
    --wood-dark:#2b1d15;
    --wood-mid:#4a3325;
    --wood-light:#5e4331;
    --blue:#33a6d7;
    --blue-deep:#3277b5;
    --cream:#f4efe6;
    --red:#d9312b;
    --white:#ffffff;
  }
  *{margin:0;padding:0;box-sizing:border-box}
  html,body{width:1200px;height:2596px;overflow:hidden}
  body{
    font-family:"Amatic SC",cursive;
    font-weight:700;
    color:var(--cream);
    background:
      repeating-linear-gradient(90deg,rgba(0,0,0,.08) 0 3px,transparent 3px 58px),
      linear-gradient(160deg,var(--wood-light) 0%,var(--wood-mid) 40%,var(--wood-dark) 100%);
  }
  .menu{position:relative;width:1200px;height:2596px}
  .abs{position:absolute}

  .menu-title{left:0;top:80px;width:1200px;text-align:center;font-size:96px;color:var(--blue);line-height:1;font-weight:700}
  .menu-subtitle{left:320px;top:192px;width:560px;height:54px;background:var(--white);color:var(--blue-deep);
    font-size:40px;text-align:center;line-height:54px;letter-spacing:1px}

  .intro{left:88px;width:840px;font-size:36px;line-height:44px}
  .intro .dish{color:var(--blue);font-size:48px}

  .price-tag{left:950px;width:164px;text-align:center}
  .price-tag .label{background:var(--red);color:var(--white);font-size:24px;line-height:30px;letter-spacing:1px}
  .price-tag .amount{margin-top:12px;border:2px solid var(--cream);font-size:60px;line-height:74px;color:var(--cream)}
  .price-tag .rule{height:8px;background:var(--red);margin-top:8px}

  .photo-gyros{left:690px;top:610px;width:490px;height:250px;border-radius:50%;
    background:radial-gradient(ellipse at 45% 45%,#8a5a2e 0%,#c9862f 35%,#d9443a 60%,#eeeae2 72%)}
  .photo-skewers{left:540px;top:1640px;width:640px;height:240px;border-radius:14px;
    background:linear-gradient(160deg,#f2f0ea 0%,#d6a24a 30%,#a9632c 55%,#e9c170 75%,#f2f0ea 100%)}
  .seal{left:510px;top:590px;width:190px;height:190px;border-radius:50%;background:var(--blue-deep);
    border:6px solid var(--white)}

  .section-head{font-size:58px;color:var(--blue);line-height:1;font-weight:700}
  .options{font-size:30px;line-height:38px;white-space:nowrap}
  .options .note{position:absolute;left:0;top:0}
  .options .row{display:flex}
  .options .name{text-align:right;padding-right:12px}
  .options .price{width:90px}
  .opt-left .name{width:400px}
  .opt-right .name{width:340px}
  .opt-right{line-height:54px}

  .divider{left:30px;top:1280px;width:1140px;height:24px}

  .brand{left:0;top:2380px;width:1200px;text-align:center;font-size:64px;line-height:1;color:var(--white)}
</style>
</head>
<body>
<main class="menu">
  <h1 class="abs menu-title">Open Souvlaki Platters</h1>
  <div class="abs menu-subtitle">CUSTOMIZED TO YOUR OWN TASTE</div>

  <p class="abs intro" style="top:340px"><span class="dish">Gyros Platter</span> Traditional Greek Juicy Pork or Chicken Gyros – 200 g. Generous portion served with refreshing tzatziki sauce, pita bread, fries, onion, tomatoes and lettuce. A great selection of ingredients make it a delicious complete meal!</p>

  <div class="abs price-tag" style="top:420px">
    <div class="label">STARTING FROM</div>
    <div class="amount">£ 13.50</div>
    <div class="rule"></div>
  </div>

  <div class="abs photo-gyros" role="img" aria-label="Gyros platter with fries, tomatoes, onion and pita on a white plate"></div>
  <div class="abs seal" role="img" aria-label="Round badge"></div>

  <h2 class="abs section-head" style="left:88px;top:820px">Gyros Option 200g</h2>
  <div class="abs options opt-left" style="left:88px;top:900px;width:500px">
    <span class="note">(Choose one)</span>
    <div class="row"><span class="name">Chicken:</span><span class="price">£ -</span></div>
    <div class="row"><span class="name">Pork:</span><span class="price">£ -</span></div>
    <div class="row"><span class="name">Gyros Chicken:</span><span class="price">£ 1.00</span></div>
    <div class="row"><span class="name">Gyros Pork:</span><span class="price">£ 3.50</span></div>
    <div class="row"><span class="name">Gyros Mixed (Chicken&amp;Pork):</span><span class="price">£ 3.50</span></div>
    <div class="row"><span class="name">Kebab:</span><span class="price">£ 4.00</span></div>
  </div>

  <h2 class="abs section-head" style="left:660px;top:980px">Extras</h2>
  <div class="abs options opt-right" style="left:660px;top:1050px;width:440px">
    <span class="note">(Choose any)</span>
    <div class="row"><span class="name">Haloumi:</span><span class="price">£ 3.50</span></div>
    <div class="row"><span class="name">Tzatziki:</span><span class="price">£ 3.00</span></div>
    <div class="row"><span class="name">Pita:</span><span class="price">£ 1.00</span></div>
  </div>

  <svg class="abs divider" viewBox="0 0 1140 24" aria-hidden="true">
    <line x1="20" y1="12" x2="1120" y2="12" stroke="#f4efe6" stroke-width="4" stroke-dasharray="14 10"/>
    <polygon points="0,12 18,2 18,22" fill="#f4efe6"/>
    <polygon points="1140,12 1122,2 1122,22" fill="#f4efe6"/>
  </svg>

  <p class="abs intro" style="top:1370px"><span class="dish">Skewers Platter</span> Delicious Skewers or Kebab – 2 pcs. Homemade souvlaki is taken from the best part of the meat to create the perfect succulent grilled experience. Served with fries or salad and pita bread.</p>

  <div class="abs price-tag" style="top:1440px">
    <div class="label">STARTING FROM</div>
    <div class="amount">£ 10.00</div>
    <div class="rule"></div>
  </div>

  <div class="abs photo-skewers" role="img" aria-label="Grilled chicken skewers with fries and pita on a platter"></div>

  <h2 class="abs section-head" style="left:88px;top:1760px">Skewers Option 2 pcs</h2>
  <div class="abs options opt-left" style="left:88px;top:1840px;width:500px">
    <span class="note">(Choose one)</span>
    <div class="row"><span class="name">Chicken:</span><span class="price">£ -</span></div>
    <div class="row"><span class="name">Pork:</span><span class="price">£ -</span></div>
    <div class="row"><span class="name">Kebab (Lamb&amp;Beef):</span><span class="price">£ -</span></div>
    <div class="row"><span class="name">Upgrade to 3 pcs. any:</span><span class="price">£ 3.00</span></div>
  </div>

  <h2 class="abs section-head" style="left:660px;top:1930px">Extras</h2>
  <div class="abs options opt-right" style="left:660px;top:2010px;width:440px">
    <span class="note">(Choose any)</span>
    <div class="row"><span class="name">Haloumi:</span><span class="price">£ 3.50</span></div>
    <div class="row"><span class="name">Tzatziki:</span><span class="price">£ 3.00</span></div>
    <div class="row"><span class="name">Pita:</span><span class="price">£ 1.00</span></div>
  </div>

  <h2 class="abs section-head" style="left:88px;top:2090px">Sides</h2>
  <div class="abs options opt-left" style="left:88px;top:2170px;width:500px">
    <span class="note">(Choose one)</span>
    <div class="row"><span class="name">Fries:</span><span class="price">£ -</span></div>
    <div class="row"><span class="name">Side Salad:</span><span class="price">£ 2.50</span></div>
  </div>

  <div class="abs brand">Olive Branch Kitchen</div>
</main>
</body>
</html>
```